Business Card for staff member of football club SC Brenval

I would like to get a business card template for all staff member of our soccer club.

The card should use as much as possible the 2 colors of the club : Red which is the main color and blue which is the alternative color. It can be balanced between the two like our logo.

I prefer simple and lean design.

Contact Information for Business Card

Bussiness card should have all main stuff as describe here below in must have.

Font styles to use
Sans Serif

Requirements
Must have
• Name : Laurent DESPRATIN
Fonction : Président
Mobile : +41 xx xxx xx xx
Email : first.lastname@scbrenval.ch
Adresse of the club : SC Brenval, 1873 Brenval
Website of the club : www.scbrenval.ch
Nice to have
• Version with and without picture of the staff member

A version for men, a version for women staff member.

```html
<!DOCTYPE html>
<html lang="fr">
<head>
<meta charset="utf-8">
<title>SC Brenval – Carte de visite</title>
<link href="https://fonts.googleapis.com/css2?family=Quicksand:wght@700&family=Roboto:wght@500;700&display=swap" rel="stylesheet">
<style>
  :root {
    --club-red: #e8283f;
    --club-blue: #1a8fd0;
    --ink: #222;
    --paper: #f7f7f7;
    --stage: #e4e4e4;
  }
  * { box-sizing: border-box; margin: 0; padding: 0; }
  html, body { width: 1200px; height: 675px; overflow: hidden; }
  body {
    background: var(--stage);
    display: flex;
    align-items: center;
    justify-content: center;
    gap: 40px;
    font-family: "Roboto", Arial, sans-serif;
  }
  .card {
    position: relative;
    width: 540px;
    height: 308px;
    border-radius: 14px;
    overflow: hidden;
    box-shadow: 0 6px 18px rgba(0,0,0,.12);
  }
  .card-front { background: var(--paper); }
  .card-front .graphics { position: absolute; inset: 0; }

  .club-mark {
    position: absolute; left: 38px; top: 52px;
    display: flex; align-items: center; gap: 8px;
    font-family: "Roboto", Arial, sans-serif;
    font-weight: 700; font-size: 22px; color: var(--club-red);
  }
  .club-mark .mark-square { width: 14px; height: 14px; background: var(--club-blue); }

  .identity {
    position: absolute; right: 30px; top: 72px; text-align: right;
    font-family: "Quicksand", Arial, sans-serif;
  }
  .identity .person-name {
    color: var(--club-red); font-size: 20px; letter-spacing: .5px; text-transform: uppercase;
  }
  .identity .person-role {
    color: var(--club-blue); font-size: 12px; letter-spacing: 1px; text-transform: uppercase; margin-top: 2px;
  }

  .contact-list {
    position: absolute; left: 348px; top: 150px; list-style: none;
    font-weight: 500; font-size: 12px; color: var(--ink);
  }
  .contact-list li { display: flex; align-items: center; gap: 8px; height: 19px; }
  .contact-list svg { width: 11px; height: 11px; flex: none; fill: var(--club-blue); }

  .card-back .back-mark {
    position: absolute; inset: 0;
    display: flex; align-items: center; justify-content: center; gap: 10px;
    font-family: "Roboto", Arial, sans-serif; font-weight: 700; font-size: 38px; color: #fff;
  }
  .card-back .back-mark .mark-square { width: 22px; height: 22px; background: #fff; }
</style>
</head>
<body>

  <section class="card card-front" aria-label="Recto de la carte">
    <svg class="graphics" viewBox="0 0 540 308" aria-hidden="false">
      <defs>
        <linearGradient id="portraitTone" x1="0" y1="0" x2="0" y2="1">
          <stop offset="0" stop-color="#c9c3bd"/>
          <stop offset="1" stop-color="#3a3a40"/>
        </linearGradient>
      </defs>
      <polygon class="band-red" points="0,252 228,252 252,274 0,274" fill="var(--club-red)"/>
      <polygon class="band-blue" points="262,278 540,278 540,298 284,298" fill="var(--club-blue)"/>
      <path class="portrait" role="img" aria-label="Photo portrait du membre du staff"
            d="M224 104 H322 V211 L273 240 L224 211 Z" fill="url(#portraitTone)"/>
      <path class="frame-red" d="M273 249 L215 215 V95 H273" fill="none" stroke="var(--club-red)" stroke-width="5"/>
      <path class="frame-blue" d="M273 95 H331 V215 L273 249" fill="none" stroke="var(--club-blue)" stroke-width="5"/>
    </svg>

    <div class="club-mark"><span>SC Brenval</span><span class="mark-square"></span></div>

    <div class="identity">
      <p class="person-name">Laurent Despratin</p>
      <p class="person-role">Président</p>
    </div>

    <ul class="contact-list">
      <li><svg viewBox="0 0 12 12"><path d="M6 0a4 4 0 0 0-4 4c0 3 4 8 4 8s4-5 4-8a4 4 0 0 0-4-4zm0 5.5A1.5 1.5 0 1 1 6 2.5a1.5 1.5 0 0 1 0 3z"/></svg>SC Brenval, 1873 Brenval</li>
      <li><svg viewBox="0 0 12 12"><path d="M2.5 0.5l2 2.5-1.2 1.5a7 7 0 0 0 4.2 4.2L9 7.5l2.5 2-1.5 2C5 11.5 0.5 7 0.5 2z"/></svg>+41 27 555 18 64</li>
      <li><svg viewBox="0 0 12 12"><path d="M0 2h12v8H0zm1 1v.3l5 3.2 5-3.2V3z"/></svg>first.lastname@scbrenval.ch</li>
      <li><svg viewBox="0 0 12 12"><path d="M6 0a6 6 0 1 0 0 12A6 6 0 0 0 6 0zm0 1.2c.7.8 1.2 2.2 1.3 4.2H4.7C4.8 3.4 5.3 2 6 1.2zM1.3 6.6h2.3c.1 1.6.5 3 1.1 4A4.8 4.8 0 0 1 1.3 6.6zm0-1.2A4.8 4.8 0 0 1 4.7 1.4c-.6 1-1 2.4-1.1 4zM6 10.8c-.7-.8-1.2-2.2-1.3-4.2h2.6c-.1 2-.6 3.4-1.3 4.2zm1.3-.2c.6-1 1-2.4 1.1-4h2.3a4.8 4.8 0 0 1-3.4 4zm1.1-5.2c-.1-1.6-.5-3-1.1-4a4.8 4.8 0 0 1 3.4 4z"/></svg>www.scbrenval.ch</li>
    </ul>
  </section>

  <section class="card card-back" aria-label="Verso de la carte">
    <svg class="graphics" viewBox="0 0 540 308" style="position:absolute;inset:0" aria-hidden="true">
      <rect width="540" height="308" fill="var(--club-red)"/>
      <polygon points="0,0 540,0 540,90 0,250" fill="var(--club-blue)"/>
    </svg>
    <div class="back-mark"><span>SC Brenval</span><span class="mark-square"></span></div>
  </section>

</body>
</html>
```